Travel Company is looking for a STAND OUT Business Card

I need a unique Business Card that will truly stand out. Nothing too busy. Simple is good, right? Not looking for a standard design either. No cookie cutter layout. We are a Travel Company that works more with Companies than Travelers. I had an idea to focus and emphasis on the 2 logo a bit more. This is not necessary, however thought it would look interesting. I am just looking for something interesting and a bit different. Does't have to completely off the wall crazy, just not your run of the mill business card.

Target Market(s)

Hoteliers, Resort Management, Call Centers, Executives, Travelers, Families, Businesses

Industry/Entity Type

Hospitality

Contact Information for Business Card

President/CEO - Marcus T Bellamy (title not necessary if design doesn't allow for it)
contact - (407) 555-0186
email - mbellamy@wayfarenow.example
address - 4812 Quillmore Ave #164
Orlando, FL 32804
website - www.wayfarenow.example

Font styles to use
Serif
Other font styles liked:
• Avenir Next LT Pro BOLD

Requirements
Must have
• simple look and design. Unique design
Nice to have
• I attached the 2 logo separate from the main logo. This can be used separately from the Main Logo, together with the main logo or as main logo. I included the logo font. Use it or not, designers choice.
Should not have
• cookie cutter design. Little use of red other than the logo

```html
<!DOCTYPE html>
<html lang="en">
<head>
<meta charset="utf-8">
<title>Wayfare Now — Business Card</title>
<link href="https://fonts.googleapis.com/css2?family=Arimo:wght@400;700&display=swap" rel="stylesheet">
<style>
  :root {
    --backdrop: #b1b1b1;
    --paper: #f4f4f4;
    --paper-edge: #e6e6e6;
    --ink: #111111;
    --accent: #e31e24;
    --rule: #8a8a8a;
  }
  html, body {
    margin: 0;
    padding: 0;
    width: 1200px;
    height: 1050px;
    overflow: hidden;
    background: var(--backdrop);
    font-family: "Arimo", Arial, sans-serif;
    color: var(--ink);
  }
  .card {
    position: absolute;
    left: 264px;
    width: 672px;
    height: 383px;
    background: radial-gradient(ellipse at center, #fbfbfb 0%, var(--paper) 55%, var(--paper-edge) 100%);
    overflow: hidden;
  }
  .card--front { top: 111px; }
  .card--back { top: 574px; }

  .brand {
    position: absolute;
    display: flex;
    align-items: center;
    gap: 10px;
    font-weight: 700;
    color: var(--ink);
    white-space: nowrap;
    letter-spacing: -0.5px;
  }
  .brand__dot {
    border-radius: 50%;
    background: var(--accent);
    flex: none;
  }
  .card--front .brand {
    left: 212px;
    top: 169px;
    transform: translate(-50%, -50%);
    font-size: 36px;
  }
  .card--front .brand__dot { width: 22px; height: 22px; }

  .divider {
    position: absolute;
    left: 355px;
    top: 53px;
    width: 1px;
    height: 252px;
    background: linear-gradient(to bottom, transparent, var(--rule) 15%, var(--rule) 85%, transparent);
  }

  .contact {
    position: absolute;
    left: 384px;
    top: 0;
    font-size: 16px;
    line-height: 1;
  }
  .contact__name {
    position: absolute;
    top: 88px;
    margin: 0;
    font-size: 21px;
    font-weight: 400;
    color: var(--accent);
    white-space: nowrap;
  }
  .contact__title {
    position: absolute;
    top: 112px;
    margin: 0;
    font-size: 16px;
    white-space: nowrap;
  }
  .contact__list {
    position: absolute;
    top: 159px;
    margin: 0;
    padding: 0;
    list-style: none;
  }
  .contact__item {
    display: flex;
    align-items: center;
    gap: 9px;
    height: 19.5px;
    white-space: nowrap;
  }
  .contact__icon { width: 14px; height: 14px; flex: none; }
  .contact__address {
    position: absolute;
    top: 245px;
    margin: 0;
    font-style: normal;
    line-height: 20px;
    white-space: nowrap;
  }

  .band-rule {
    position: absolute;
    left: 0;
    top: 344px;
    width: 100%;
    height: 3px;
    background: var(--accent);
  }
  .band {
    position: absolute;
    left: 0;
    top: 350px;
    width: 100%;
    height: 33px;
    background: #000;
  }

  .card--back .brand {
    left: 336px;
    top: 191px;
    transform: translate(-50%, -50%);
    font-size: 52px;
    gap: 14px;
  }
  .card--back .brand__dot { width: 32px; height: 32px; }
</style>
</head>
<body>

<section class="card card--front" aria-label="Business card front">
  <div class="brand"><span class="brand__name">Wayfare Now</span><span class="brand__dot"></span></div>

  <div class="divider"></div>

  <div class="contact">
    <h1 class="contact__name">Marcus T Bellamy</h1>
    <p class="contact__title">President/CEO</p>

    <ul class="contact__list">
      <li class="contact__item">
        <svg class="contact__icon" viewBox="0 0 24 24" aria-hidden="true">
          <path fill="var(--accent)" d="M6.6 10.8a15.1 15.1 0 0 0 6.6 6.6l2.2-2.2a1 1 0 0 1 1-.25 11.4 11.4 0 0 0 3.6.57 1 1 0 0 1 1 1V20a1 1 0 0 1-1 1A17 17 0 0 1 3 4a1 1 0 0 1 1-1h3.5a1 1 0 0 1 1 1c0 1.25.2 2.45.57 3.57a1 1 0 0 1-.25 1z"/>
        </svg>
        <span>(407) 555-0186</span>
      </li>
      <li class="contact__item">
        <svg class="contact__icon" viewBox="0 0 24 24" aria-hidden="true">
          <rect x="2" y="5" width="20" height="14" fill="var(--accent)"/>
          <path d="M2 5l10 8 10-8M2 19l7-7M22 19l-7-7" fill="none" stroke="#fff" stroke-width="1.6"/>
        </svg>
        <span>mbellamy@wayfarenow.example</span>
      </li>
      <li class="contact__item">
        <svg class="contact__icon" viewBox="0 0 24 24" aria-hidden="true">
          <g fill="none" stroke="var(--accent)" stroke-width="1.6">
            <circle cx="12" cy="12" r="10"/>
            <ellipse cx="12" cy="12" rx="4.5" ry="10"/>
            <path d="M2 12h20M4 6.5h16M4 17.5h16"/>
          </g>
        </svg>
        <span>www.wayfarenow.example</span>
      </li>
    </ul>

    <address class="contact__address">4812 Quillmore Ave #164<br>Orlando, FL 32804</address>
  </div>

  <div class="band-rule"></div>
  <div class="band"></div>
</section>

<section class="card card--back" aria-label="Business card back">
  <div class="brand"><span class="brand__name">Wayfare Now</span><span class="brand__dot"></span></div>
</section>

</body>
</html>
```